Web app for job market trends **

We are building a website where users come to see what skills they will need for their career. The content of the page is data-driven, so the site should have the feel of a set of data dashboards. The data is collected and processed using machine learning. The main idea is for the user to come in and spend some minutes exploring, scrolling and clicking around.
The task is to design a website with four pages:
Front page
Early career page
Skill trends page
Skills Page
Each of these is described in attached files, along with example data
We need the resulting files to be exported also to uncompressed PNG, and in the case of vector graphics, to SVG.
Target Market(s)
People Looking to start a Career and Policy makers.
Industry/Entity Type
Human Resource
Number of Pages Required
4 page
Look and feel

```html
<!DOCTYPE html>
<html lang="en">
<head>
<meta charset="utf-8">
<title>TalentTide — Your personal guide to the skill trends on the job market</title>
<link href="https://fonts.googleapis.com/css2?family=Lato:ital,wght@0,400;0,700;0,900;1,700&display=swap" rel="stylesheet">
<style>
:root{
  --blue:#1f47b0;
  --blue-deep:#0f2f8f;
  --blue-light:#3d78e0;
  --orange:#ff7a00;
  --ink:#2b2b2b;
  --text:#333;
  --grey-bg:#f2f2f2;
  --footer:#333333;
  --white:#fff;
}
*{box-sizing:border-box;margin:0;padding:0}
html,body{width:1200px;height:3862px;overflow:hidden}
body{position:relative;background:var(--white);font-family:'Lato',sans-serif;color:var(--text)}
.abs{position:absolute}
.shape{position:absolute;left:0;top:0}
.photo{position:absolute;border-radius:22px;box-shadow:0 10px 24px rgba(0,0,0,.18)}

.brand{font-weight:900;font-size:36px;color:var(--ink);letter-spacing:-.3px}
.nav{position:absolute;top:68px;left:648px}
.nav a{position:absolute;top:0;white-space:nowrap;color:var(--white);font-size:15px;font-weight:700;text-decoration:none;letter-spacing:.3px}

.hero-title{left:75px;top:220px;font-size:90px;font-weight:900;color:var(--blue);line-height:1}
.hero-sub{left:77px;top:320px;width:320px;font-size:29px;font-weight:700;color:var(--ink);line-height:36px}
.btn{position:absolute;display:flex;align-items:center;justify-content:center;background:var(--orange);color:var(--white);font-weight:700;border-radius:26px;text-decoration:none}
.quote{left:74px;top:812px;font-size:19.5px;font-style:italic;font-weight:700;color:var(--blue-deep);line-height:38px;white-space:nowrap}

.band{position:absolute;left:0;width:1200px;background:var(--grey-bg)}
.section-title{position:absolute;left:0;width:1200px;text-align:center;font-size:39px;font-weight:700;color:var(--ink)}
.step{position:absolute;width:74px;height:74px;border-radius:50%;background:var(--blue);color:var(--white);font-size:33px;display:flex;align-items:center;justify-content:center}
.search{left:75px;top:1295px;width:330px;height:46px;border:1px solid #ccc;border-radius:23px;background:var(--white);font-size:14px;color:#555;display:flex;align-items:center;padding:0 18px}
.search .lang{margin-left:auto;border-left:1px solid #777;padding-left:12px;display:flex;align-items:center;gap:12px}
.preview{position:absolute;border:1px solid #ccc}

.block-title{position:absolute;font-size:30px;font-weight:900;color:var(--blue)}
.body-copy{position:absolute;font-size:14.3px;line-height:27.8px;color:var(--text);white-space:nowrap}
.body-copy p+p{margin-top:12px}

.about-copy{left:0;top:2798px;width:1200px;text-align:center;font-size:14.3px;line-height:27.8px;white-space:nowrap}
.about-copy p+p{margin-top:8px}
.portrait{position:absolute;width:150px;height:150px;border-radius:50%}

.partner{position:absolute;display:flex;flex-direction:column;align-items:center;justify-content:center;gap:12px}
.partner-name{font-size:22px;font-weight:700;color:var(--ink)}

.footer{position:absolute;left:0;top:3655px;width:1200px;height:207px;background:var(--footer);color:var(--white)}
.footer h4{position:absolute;font-size:19px;font-weight:700}
.footer .small{position:absolute;font-size:14px;line-height:27px}
.footer .legal{font-size:13.5px;line-height:26px}
.social{position:absolute;width:24px;height:24px;border-radius:4px;background:var(--white)}
.email-input{position:absolute;left:842px;top:77px;width:283px;height:42px;border-radius:21px;background:var(--white);color:#333;font-size:13px;display:flex;align-items:center;padding-left:21px}
</style>
</head>
<body>

<!-- HERO -->
<svg class="shape" width="1200" height="760" viewBox="0 0 1200 760" aria-hidden="true">
  <path d="M472 0 L1200 0 L1200 620 C1120 672 1020 742 915 738 C830 734 770 690 742 640 L555 132 Z" fill="var(--blue-deep)"/>
  <path d="M472 0 L505 0 L560 132 L540 132 Z" fill="var(--blue-light)"/>
  <path d="M1200 600 L1200 640 C1130 680 1060 700 1010 705 C1080 690 1140 650 1200 600 Z" fill="var(--blue-light)"/>
</svg>

<div class="abs brand" style="left:75px;top:56px">TalentTide</div>
<nav class="nav">
  <a style="left:0">EARLY CAREER</a>
  <a style="left:150px">SKILL TRENDS</a>
  <a style="left:294px">SKILLS</a>
  <a style="left:384px">CONTACT US</a>
</nav>

<div class="photo" role="img" aria-label="Photo of a smiling woman drawing on paper at a desk beside a colleague" style="left:468px;top:132px;width:657px;height:508px;background:linear-gradient(135deg,#c9ccd4 0%,#9aa0ac 40%,#7a5040 60%,#d8dde3 100%)"></div>

<h1 class="abs hero-title">TalentTide</h1>
<p class="abs hero-sub">Your personal guide to the skill trends on the job market</p>
<a class="btn" style="left:75px;top:462px;width:190px;height:51px;font-size:19px">Read More</a>

<p class="abs quote">“We enable deep and unbiased analysis of the skill demands in the job market. Using deep learning techniques,<br>we achieve understanding of job advertisements to extract the most relevant information for you. We combine these analysis with<br>the most complete structural knowledge repositories to deliver analytics, discover trends and provide recommendations for<br>personal professional development, as well as insightful job market overviews!”</p>

<!-- THREE WAYS -->
<section class="band" style="top:1032px;height:428px"></section>
<h2 class="section-title" style="top:1068px">Three different ways to proceed</h2>
<div class="step" style="left:203px;top:1145px">1</div>
<div class="step" style="left:563px;top:1145px">2</div>
<div class="step" style="left:926px;top:1145px">3</div>

<div class="abs search">Enter a skill or a job title
  <span class="lang">EN
    <svg width="10" height="7" viewBox="0 0 10 7" aria-hidden="true"><path d="M1 1 L5 5 L9 1" stroke="#333" stroke-width="2" fill="none"/></svg>
  </span>
</div>

<div class="preview" role="img" aria-label="Preview of the skill trends chart page" style="left:435px;top:1257px;width:333px;height:120px;background:linear-gradient(180deg,#ffffff 0%,#eef1f8 100%)"></div>

<div class="preview" role="img" aria-label="Preview of an annotated job advertisement page" style="left:898px;top:1233px;width:128px;height:168px;background:linear-gradient(180deg,#ffffff 0%,#eceef4 100%)"></div>

<!-- OUR APPLICATION -->
<h2 class="section-title" style="top:1508px">Our Application</h2>

<svg class="shape" style="top:1599px" width="1200" height="520" viewBox="0 0 1200 520" aria-hidden="true">
  <path d="M0 0 H452 L400 70 V440 C320 470 240 476 160 468 C90 460 40 440 0 420 Z" fill="var(--blue-deep)"/>
  <path d="M0 420 C40 446 90 468 150 478 C110 496 50 498 0 490 Z" fill="var(--blue-light)"/>
</svg>
<div class="photo" role="img" aria-label="Photo of a hiker with a backpack facing a snowy mountain peak" style="left:75px;top:1629px;width:513px;height:396px;background:linear-gradient(180deg,#9aa3ad 0%,#c8ced4 45%,#e8eaec 75%,#f2f3f4 100%)"></div>

<h3 class="block-title" style="left:616px;top:1642px">Challenges</h3>
<div class="body-copy" style="left:615px;top:1693px">
  <p>Choosing the correct occupation plays an increasingly important role in our<br>lives. Nowadays we consider an occupation as one of our fundamental<br>rights. Yet, with the complexity of the modern technologies and job markets<br>it is challenging to guarantee equal access to the market for everyone.”</p>
  <p>The challenges include the knowledge of languages, personal traits,<br>different understanding of requirements and different assessments of<br>personal strengths. On the other end, business owners and recruitment<br>professionals invest lots of effort to find suitable candidates for their job<br>openings. How do we improve the situation, overcome the challenges and<br>enable efficient, unbiased analysis of job advertisements without<br>the need to change the existing practices?”</p>
</div>

<svg class="shape" style="top:2110px" width="1200" height="520" viewBox="0 0 1200 520" aria-hidden="true">
  <path d="M750 0 H1200 V470 C1130 505 1030 515 950 495 C890 480 850 455 820 430 V60 Z" fill="var(--blue-deep)"/>
  <path d="M1200 440 V505 C1150 518 1090 520 1040 512 C1100 500 1160 475 1200 440 Z" fill="var(--blue-light)"/>
</svg>
<div class="photo" role="img" aria-label="Illustration of a man looking at a glowing network sphere surrounded by analytics icons" style="left:615px;top:2142px;width:510px;height:393px;background:radial-gradient(circle at 50% 40%,#e8f0fa 0%,#b8cde6 45%,#8eaed4 100%)"></div>

<h3 class="block-title" style="left:76px;top:2172px">How we do this</h3>
<div class="body-copy" style="left:76px;top:2221px">
  <p>We employ machine learning. Machines do not have personal preferences<br>or biases. The impressive progress of natural language processing and deep<br>neural networks power our algorithms to precisely recognize and extract<br>the most important pieces of information. We use manually designed<br>ontologies that set the frames of the analysis and guide the machine in this<br>process. However, machines (and also we ourselves) still miss a lot of<br>&nbsp;background information about our complex professional world -- no one is<br>perfect (yet). To fill in this gap we use the most complete structural<br>knowledge sources to serve as background knowledge and provide<br>additional information about the subject area.</p>
</div>

<!-- ABOUT -->
<section class="band" style="top:2678px;height:667px"></section>
<h2 class="section-title" style="top:2741px">About Us</h2>
<div class="abs about-copy">
  <p>This application is a free social project powered by 3 enthusiast. We are experts in Natural Language Processing and Semantic Web with a record of<br>50+ scientific publications at top conferences and journals . We also have training and work experience in HR, and, most importantly passion for the job<br>market. We all have migrant backgrounds and we know how difficult and important it might be to find your place in any new professional environment.<br>Therefore, we strive to provide better professional opportunities, equal access and fair treatment for everyone</p>
  <p>At the moment the project is completely funded by us. This not only includes the maintenance and further development, but also the costs of the<br>infrastructure. If you like it and want us to continue, please, support us. Your every donation counts.</p>
</div>
<div class="portrait" role="img" aria-label="Portrait photo of the first team member" style="left:345px;top:3018px;background:linear-gradient(160deg,#d9d9d9,#8a8a8a)"></div>
<div class="portrait" role="img" aria-label="Portrait photo of the second team member" style="left:525px;top:3018px;background:linear-gradient(160deg,#d0d4da,#6e7480)"></div>
<div class="portrait" role="img" aria-label="Portrait photo of the third team member" style="left:707px;top:3018px;background:linear-gradient(160deg,#d8d2cc,#7a6a60)"></div>
<a class="btn" style="left:505px;top:3222px;width:191px;height:51px;font-size:19px">Donate Now</a>

<!-- POWERED BY -->
<h2 class="section-title" style="top:3393px">Powered by</h2>
<div class="partner" style="left:372px;top:3465px;width:195px;height:135px">
  <div style="width:40px;height:40px;background:#a0112a"></div>
  <span class="partner-name">OpenFacts</span>
</div>
<div class="partner" style="left:600px;top:3465px;width:240px;height:135px">
  <div style="width:40px;height:40px;background:#0e3296"></div>
  <span class="partner-name">Civic Union Fund</span>
</div>

<!-- FOOTER -->
<footer class="footer">
  <div class="abs brand" style="left:75px;top:51px;color:var(--white)">TalentTide</div>
  <div class="small legal" style="left:74px;top:98px">Copyright ©2021 Company Name<br>All Right Reserved , Terms, Privacy Policy</div>

  <h4 style="left:415px;top:36px">Site Map</h4>
  <div class="small" style="left:415px;top:64px">Early career<br>Skill trends<br>Skills<br>Contact us</div>

  <h4 style="left:639px;top:36px">Contact Us</h4>
  <div class="small" style="left:639px;top:64px">hello@talenttide.example</div>
  <span class="social" style="left:639px;top:107px" aria-label="Social profile"></span>
  <span class="social" style="left:688px;top:107px" aria-label="Social profile"></span>

  <h4 style="left:845px;top:36px">Email Sign Up</h4>
  <div class="email-input">Email Address</div>
  <a class="btn" style="left:842px;top:127px;width:136px;height:42px;font-size:19px;border-radius:21px">Sign Up</a>
</footer>

</body>
</html>
```